Construction Route to Market Infographic

We need an infographic for a large wall in our office. We are Drummet Studio and we are a marketing agency for the Construction industry. We want to help show our customers the route to market for their products along with the supply chain. We want to do this in a graphical way that is lively, professional and easy to follow. Drummet Studio brand guidelines should be adhered to. The final design should communicate that we know what we are talking about and you are safe using us a s your marketing agency. We will help you sell your product.

http://www.drummetstudio.co.uk

Target Market(s)

Building Product Manufacturers

Industry/Entity Type

Construction

Font styles to use
Other font styles liked:
• Century Old Style - Regular is the brand font. A complimentary font can also be used.

Requirements
Must have
• Must be in vector format
• Must have company logos where a company is mentioned
• Must be lively and engaging

```html
<!DOCTYPE html>
<html lang="en">
<head>
<meta charset="utf-8">
<title>Route to Market – Drummet Studio</title>
<link rel="stylesheet" href="https://fonts.googleapis.com/css2?family=Roboto:wght@400;700;900&family=Roboto+Condensed:wght@400;700&display=swap">
<style>
:root{
  --bg:#6d6e71;
  --ink:#1f2a30;
  --red:#e8383d;
  --red-dark:#c9202a;
  --orange:#f07f22;
  --orange-light:#f7a33a;
  --pr-blue:#27a3d5;
  --slate:#46535e;
  --grey:#a2aaac;
  --teal:#1d9c93;
  --teal-dark:#137a73;
  --blue:#1f79c1;
  --blue-dark:#145b9a;
  --white:#ffffff;
  --band-a:#1ebfd0;
  --band-b:#1466b8;
  --link:#f08a5d;
}
*{margin:0;padding:0;box-sizing:border-box}
html,body{width:1200px;height:1000px;overflow:hidden;background:var(--bg)}
.canvas{position:relative;width:1200px;height:1000px;background:var(--bg);font-family:"Roboto",Arial,sans-serif;color:var(--white)}
.shapes{position:absolute;inset:0}
.flag{position:absolute;display:flex;align-items:center;justify-content:center;text-align:center;font-weight:700;color:var(--white);
  background:linear-gradient(135deg,#f25a5c,var(--red-dark));border-radius:0 48px 0 48px;font-size:15px;line-height:1.15;letter-spacing:.2px}
.flag--route{left:575px;top:10px;width:150px;height:98px}
.flag--architect{left:108px;top:422px;width:150px;height:100px}
.flag--maker{left:1015px;top:400px;width:150px;height:100px;justify-content:flex-start;padding-left:14px;text-align:left}
.race{position:absolute;left:600px;top:113px;width:88px;height:37px;background:#111;border-radius:9px;font-weight:900;font-size:14px;
  display:flex;align-items:center;justify-content:center}
.stage-label{position:absolute;font-weight:700;font-size:15px;text-align:center;width:100px;transform:translateX(-50%)}
.pin-label{position:absolute;transform:translateX(-50%);font-weight:700;text-align:center;white-space:nowrap}
.pin-label--rep{left:280px;top:379px;font-size:7.5px;color:#e25b22}
.pin-label--pr{left:382px;top:337px;font-size:14px;color:#2485c2}
.pin-label--camp{left:470px;top:334px;font-size:6.5px;color:var(--ink)}
.pin-label--lead{left:566px;top:336px;font-size:5.5px;color:#555}
.list{position:absolute;display:flex;flex-direction:column;align-items:center;text-align:center;font-family:"Roboto Condensed",Arial,sans-serif;
  font-size:8px;line-height:1.15;color:var(--white)}
.list .chev{width:9px;height:9px;border-right:2px solid var(--white);border-bottom:2px solid var(--white);transform:rotate(45deg);margin-bottom:8px}
.list p{margin:0}
.badge{display:block;background:var(--white);border-radius:2px}
.brand{font-family:"Roboto Condensed",Arial,sans-serif;font-weight:700;font-size:9px;color:var(--white)}
.brand--box{background:var(--white);color:var(--ink);padding:3px 6px;width:70px}
.list--rep{left:262px;top:496px;width:88px;gap:10px}
.list--pr{left:360px;top:455px;width:87px;gap:6px}
.list--camp{left:456px;top:452px;width:84px;gap:9px}
.list--lead{left:551px;top:454px;width:81px;gap:5px}
.list--act{left:664px;top:365px;width:88px}
.list--act .chev{margin-bottom:20px}
.list--conv{left:780px;top:354px;width:95px;gap:9px}
.list--eng{left:902px;top:352px;width:94px;gap:9px}
.band-text{position:absolute;left:165px;top:841px;font-size:15.5px;font-weight:500;line-height:1.2;letter-spacing:.2px;color:var(--white)}
</style>
</head>
<body>
<div class="canvas">
<svg class="shapes" width="1200" height="1000" viewBox="0 0 1200 1000">
  <defs>
    <linearGradient id="bandGrad" x1="0" x2="1"><stop offset="0" stop-color="var(--band-a)"/><stop offset="1" stop-color="var(--band-b)"/></linearGradient>
    <linearGradient id="tealGrad" x1="0" x2="1"><stop offset="0" stop-color="#2bb3a6"/><stop offset="1" stop-color="var(--teal-dark)"/></linearGradient>
    <linearGradient id="blueGrad" x1="0" x2="1"><stop offset="0" stop-color="#2d8fd6"/><stop offset="1" stop-color="var(--blue-dark)"/></linearGradient>
    <linearGradient id="orangeGrad" x1="0" x2="1"><stop offset="0" stop-color="var(--orange-light)"/><stop offset="1" stop-color="#e36d12"/></linearGradient>
    <marker id="head" viewBox="0 0 10 10" refX="6" refY="5" markerWidth="5" markerHeight="5" orient="auto"><path d="M0 0L10 5L0 10z" fill="var(--ink)"/></marker>
    <marker id="headO" viewBox="0 0 10 10" refX="6" refY="5" markerWidth="4" markerHeight="4" orient="auto"><path d="M0 0L10 5L0 10z" fill="var(--link)"/></marker>
  </defs>

  <line class="axis" x1="75" y1="85" x2="75" y2="940" stroke="#3d3e40" stroke-width="3"/>

  <!-- RACE links -->
  <g stroke="var(--link)" stroke-width="5" fill="none" marker-end="url(#headO)">
    <line x1="605" y1="140" x2="440" y2="188"/>
    <line x1="670" y1="150" x2="670" y2="180"/>
    <line x1="682" y1="145" x2="778" y2="180"/>
    <line x1="688" y1="138" x2="895" y2="183"/>
  </g>

  <!-- reach branches -->
  <g stroke="var(--ink)" stroke-width="7" marker-end="url(#head)">
    <line x1="370" y1="262" x2="300" y2="340"/>
    <line x1="385" y1="280" x2="385" y2="305"/>
    <line x1="428" y1="278" x2="455" y2="305"/>
    <line x1="445" y1="262" x2="540" y2="312"/>
    <line x1="690" y1="285" x2="708" y2="305"/>
    <line x1="815" y1="275" x2="823" y2="293"/>
    <line x1="935" y1="278" x2="945" y2="293"/>
  </g>

  <!-- columns -->
  <path class="col col--rep" fill="var(--orange)" d="M296 430 C300 460 350 470 350 520 L350 725 Q350 755 320 755 L290 755 Q260 755 260 725 L260 510 Q260 470 296 430Z"/>
  <path class="col col--pr" fill="var(--pr-blue)" d="M402 392 C404 415 447 420 447 455 L447 775 Q447 800 422 800 L383 800 Q358 800 358 775 L358 455 Q358 420 402 392Z"/>
  <path class="col col--camp" fill="var(--slate)" d="M498 385 C500 405 540 412 540 445 L540 745 Q540 770 515 770 L480 770 Q455 770 455 745 L455 445 Q455 412 498 385Z"/>
  <path class="col col--lead" fill="var(--grey)" d="M590 387 C592 405 632 410 632 445 L632 558 Q632 582 608 582 L574 582 Q550 582 550 558 L550 445 Q550 410 590 387Z"/>
  <path class="col col--act" fill="var(--orange)" d="M710 292 C712 312 752 318 752 345 L752 414 Q752 438 728 438 L687 438 Q663 438 663 414 L663 345 Q663 318 710 292Z"/>
  <path class="col col--conv" fill="url(#tealGrad)" d="M826 292 C830 315 875 322 875 352 L875 742 Q875 768 850 768 L803 768 Q778 768 778 742 L778 352 Q778 322 826 292Z"/>
  <path class="col col--eng" fill="url(#blueGrad)" d="M946 290 C950 312 996 320 996 350 L996 657 Q996 682 971 682 L925 682 Q900 682 900 657 L900 350 Q900 320 946 290Z"/>

  <!-- pins -->
  <g fill="var(--white)">
    <path d="M296 450 L268 405 A32 32 0 1 1 312 405Z"/>
    <circle cx="280" cy="383" r="32"/>
    <path d="M402 405 L370 360 A32 32 0 1 1 398 375Z"/>
    <circle cx="382" cy="345" r="32"/>
    <path d="M498 400 L458 352 A32 32 0 1 1 494 368Z"/>
    <circle cx="470" cy="338" r="31"/>
    <path d="M590 400 L548 355 A32 32 0 1 1 586 370Z"/>
    <circle cx="566" cy="340" r="31"/>
  </g>

  <!-- stage circles -->
  <g class="stage stage--reach">
    <circle cx="408" cy="236" r="50" fill="#fff"/>
    <circle cx="408" cy="236" r="46" fill="var(--red)"/>
    <circle cx="408" cy="236" r="36" fill="none" stroke="#f6b3b4" stroke-width="3"/>
    <circle cx="408" cy="236" r="26" fill="none" stroke="#f6b3b4" stroke-width="3"/>
    <circle cx="408" cy="236" r="15" fill="none" stroke="#f6b3b4" stroke-width="3"/>
    <line x1="410" y1="226" x2="456" y2="196" stroke="#333" stroke-width="4"/>
    <path d="M452 188 L468 190 L462 204Z" fill="#333"/>
  </g>
  <g class="stage stage--act">
    <circle cx="682" cy="242" r="40" fill="#fff"/>
    <circle cx="682" cy="242" r="37" fill="url(#orangeGrad)"/>
    <circle cx="682" cy="218" r="18" fill="#fff"/>
    <path d="M677 210 L670 218 L677 226 M671 218 H686 Q692 218 692 224" stroke="var(--orange)" stroke-width="4" fill="none"/>
  </g>
  <g class="stage stage--convert">
    <path d="M770 250 L760 275 L790 262Z" fill="#fff"/>
    <circle cx="806" cy="232" r="44" fill="#fff"/>
    <circle cx="806" cy="232" r="41" fill="url(#tealGrad)"/>
    <circle cx="806" cy="212" r="17" fill="#fff"/>
    <g fill="var(--teal)"><circle cx="798" cy="212" r="2.5"/><circle cx="806" cy="212" r="2.5"/><circle cx="814" cy="212" r="2.5"/></g>
  </g>
  <g class="stage stage--engage">
    <circle cx="926" cy="234" r="44" fill="#fff"/>
    <circle cx="926" cy="234" r="41" fill="url(#blueGrad)"/>
    <circle cx="926" cy="210" r="17" fill="#fff"/>
    <path d="M916 205 H921 L933 198 V222 L921 215 H916Z M920 215 L923 222" fill="var(--blue)" stroke="var(--blue)" stroke-width="1.5"/>
  </g>

  <!-- bottom band -->
  <path class="band" d="M75 812 H1118 L1158 860 L1118 908 H75Z" fill="url(#bandGrad)"/>
  <path d="M85 823 H1110 L1145 860 L1110 897 H85" fill="none" stroke="#bfeaf4" stroke-width="1.2" stroke-dasharray="7 4"/>
</svg>

<div class="flag flag--route">ROUTE TO MARKET</div>
<div class="race">RACE</div>
<div class="flag flag--architect">ARCHITECT</div>
<div class="flag flag--maker">PRODUCTION<br>MANUFACTURER</div>

<div class="stage-label" style="left:408px;top:240px">REACH</div>
<div class="stage-label" style="left:682px;top:248px">ACT</div>
<div class="stage-label" style="left:806px;top:228px">CONVERT</div>
<div class="stage-label" style="left:926px;top:230px">ENGAGE</div>

<div class="pin-label pin-label--rep">REPUTATION</div>
<div class="pin-label pin-label--pr">PR</div>
<div class="pin-label pin-label--camp">CAMPAIGNS</div>
<div class="pin-label pin-label--lead">LEAD ACQUISITION</div>

<div class="list list--rep">
  <span class="chev"></span>
  <p>sub-contractor influence<br>end user influence</p>
  <p>colleague or peer influence</p>
  <p>previously specified</p>
</div>

<div class="list list--pr">
  <span class="chev"></span>
  <p>Print publications -</p>
  <span class="badge" style="width:74px;height:16px" role="img" aria-label="Building Supply Guild member badge"></span>
  <p>Online Publications<br>Events exhibitions<br>sponsorship</p>
  <p>advertising</p>
  <p>SpecBook (Product Selector)</p>
  <p>ESI (Environmental Sensitivity Index)</p>
  <p>TV shows -</p>
  <span class="brand">Dream Builds</span>
  <span class="brand">Vista TV</span>
  <span class="brand">The Reveal</span>
  <p>Membership Organisations<br>Directories<br>Forums<br>Manufacturers website</p>
</div>

<div class="list list--camp">
  <span class="chev"></span>
  <p>Paid</p>
  <p>Industry trends</p>
  <p>Government Regulation Chnages</p>
  <p>Earned</p>
  <p>Pay Per Click</p>
  <p>Blog</p>
  <p>Remarketing</p>
  <p>Search Seekly</p>
  <p>Email</p>
  <p>Co-branded email</p>
  <p>online ads/banners</p>
  <p>landing pages</p>
  <p>social adverts</p>
  <p>social media</p>
</div>

<div class="list list--lead">
  <span class="chev"></span>
  <span class="brand brand--box">Planview Data</span>
  <span class="brand brand--box">Sitebrief</span>
  <p style="margin-top:3px">Leading Edge<br>Active Planning<br>Leads</p>
</div>

<div class="list list--act">
  <span class="chev"></span>
  <p>visit Website</p>
</div>

<div class="list list--conv">
  <span class="chev" style="margin-bottom:2px"></span>
  <p>Sales call/meeting</p>
  <span class="brand">Clientwise</span>
  <p>CPD<br>Factory tour</p>
  <p>Technical call/meeting</p>
  <p>read Blog</p>
  <p>read Case Studies</p>
  <p>BIM Objects</p>
  <p>CAD Drawings</p>
  <p>Spec tools</p>
  <p>product selector</p>
  <p>product comparison</p>
  <p>design consideration</p>
  <p>colour fflexibility</p>
  <p>Calculators</p>
  <p>Performance data</p>
  <p>product certification (TCA, CE etc)</p>
  <p>Building Regulations (BS, BES)</p>
  <p>Technical data</p>
</div>

<div class="list list--eng">
  <span class="chev" style="margin-bottom:2px"></span>
  <p>Testimonial</p>
  <p>Case Study</p>
  <p>White paper</p>
  <p>Lead nurturing</p>
  <p>Members area</p>
  <p>social media</p>
  <p>lead automation</p>
  <span class="brand">Nurtura</span>
  <p>Email<br>Events - road shows</p>
  <p>ebooks</p>
  <p>video case studies</p>
  <p>remarketing</p>
  <p>product launches</p>
  <p>data sheets</p>
  <p>online tools</p>
</div>

<div class="band-text">THROUGHOUT THE PROCESS A CRM WILL KEEP TRACK OF CUSTOMER INTERACTIONS - CLIENTWISE<br>VISITOR BEHAVIOUR TRACKING AND CAMPAIGN MEASUREMENT - SEEKLY METRICS</div>
</div>
</body>
</html>
```